This will turn into a huge project with mass exposure.

Tallow Crest creates soap, perfumes, rubs, lotion, etc for some of the most know brands in the market: Marisol Veil, Fern & Pebble Supply, PGR sports teams, etc.

They are going to be redesigning all logos, labels, websites and print.

They are starting with a business card and logo.

ALL designs must include a logo for Tallow Crest Holdings
Updates

Target Market(s)

Purchasers such as Marisl Veil

Industry/Entity Type

Business

Requirements
Must have
• a space for Qr code

two sided

Info:
Gavin Torlek, President
info@tallowcrest.example
555-014-2783
Nice to have
• Colors: gray background with blue and green tones. A globe that looks like an ancient map.

```html
<!DOCTYPE html>
<html lang="en">
<head>
<meta charset="utf-8">
<title>Tallow Crest Business Card</title>
<link rel="stylesheet" href="https://fonts.googleapis.com/css2?family=Cinzel&family=Federo&display=swap">
<style>
  :root {
    --page: #ffffff;
    --label-ink: #111111;
    --front-gray: #7b827d;
    --front-green: #0d6431;
    --back-olive: #969579;
    --logo-ink: #1b2a1d;
    --contact-blue: #4b5080;
    --name-green: #4d7a4b;
    --globe-cream: #e8dcc0;
    --globe-tan: #c9a86a;
    --globe-sepia: #8a6a3e;
    --glow-green: #9fd07a;
    --qr-fill: #a7a68c;
    --qr-edge: #6f6e57;
    --card-shadow: rgba(0, 0, 0, 0.6);
  }
  html, body {
    margin: 0;
    padding: 0;
    overflow: hidden;
    background: var(--page);
  }
  .canvas {
    position: relative;
    width: 1200px;
    height: 900px;
    overflow: hidden;
    background: var(--page);
  }
  .side-label {
    position: absolute;
    margin: 0;
    font-family: "Cinzel", serif;
    font-weight: 400;
    font-size: 40px;
    letter-spacing: 1px;
    color: var(--label-ink);
    line-height: 1;
  }
  .side-label--front { left: 818px; top: 86px; }
  .side-label--back { left: 253px; top: 778px; }

  .card {
    position: absolute;
    box-shadow: -7px 9px 10px var(--card-shadow);
    font-family: "Federo", sans-serif;
    overflow: hidden;
  }
  .card--front {
    left: 40px;
    top: 58px;
    width: 710px;
    height: 360px;
    background: linear-gradient(to bottom,
      var(--front-gray) 0%,
      var(--front-gray) 12%,
      var(--front-green) 49%,
      var(--front-gray) 86%,
      var(--front-gray) 100%);
  }
  .card--back {
    left: 421px;
    top: 487px;
    width: 707px;
    height: 356px;
    background: var(--back-olive);
  }

  .globe-art {
    position: absolute;
    border-radius: 50%;
  }
  .card--front .globe-art {
    left: 175px;
    top: 52px;
    width: 375px;
    height: 255px;
    background: radial-gradient(ellipse at 45% 40%,
      var(--globe-tan) 0%,
      var(--globe-sepia) 60%,
      transparent 100%);
    opacity: 0.45;
  }
  .card--back .globe-art {
    left: 86px;
    top: 53px;
    width: 215px;
    height: 150px;
    background: radial-gradient(ellipse at 40% 35%,
      var(--globe-cream) 0%,
      var(--globe-tan) 65%,
      var(--globe-sepia) 100%);
  }
  .logo-glow {
    position: absolute;
    left: 40px;
    top: 128px;
    width: 300px;
    height: 22px;
    border-radius: 50%;
    background: radial-gradient(ellipse at center,
      var(--glow-green) 0%,
      transparent 70%);
    opacity: 0.8;
  }

  .wordmark {
    position: absolute;
    margin: 0;
    font-family: "Federo", sans-serif;
    font-weight: 400;
    color: var(--logo-ink);
    white-space: nowrap;
    line-height: 1;
    text-align: center;
  }
  .card--front .wordmark {
    left: 0;
    right: 0;
    top: 165px;
    font-size: 58px;
    letter-spacing: 2px;
  }
  .card--back .wordmark {
    left: 66px;
    width: 255px;
    top: 124px;
    font-size: 24px;
    letter-spacing: 1px;
  }

  .contact {
    position: absolute;
    left: 290px;
    width: 375px;
    top: 84px;
    text-align: center;
    color: var(--contact-blue);
    font-size: 22px;
    line-height: 29px;
  }
  .contact a { color: inherit; text-decoration: none; }
  .person {
    position: absolute;
    left: 290px;
    width: 375px;
    top: 176px;
    text-align: center;
    color: var(--name-green);
  }
  .person__name {
    margin: 0;
    font-size: 46px;
    font-weight: 400;
    letter-spacing: 2px;
    line-height: 1;
    text-transform: uppercase;
  }
  .person__title {
    margin: 6px 0 0;
    font-size: 24px;
    letter-spacing: 1px;
    line-height: 1;
  }

  .qr-space {
    position: absolute;
    left: 146px;
    top: 240px;
    width: 92px;
    height: 92px;
    background: var(--qr-fill);
    border: 1px solid var(--qr-edge);
    box-sizing: border-box;
  }
</style>
</head>
<body>
<main class="canvas">
  <p class="side-label side-label--front">FRONT</p>
  <section class="card card--front" aria-label="Card front">
    <div class="globe-art" role="img" aria-label="Faded antique map globe behind the company name"></div>
    <p class="wordmark">TALLOW CREST</p>
  </section>

  <p class="side-label side-label--back">BACK</p>
  <section class="card card--back" aria-label="Card back">
    <div class="globe-art" role="img" aria-label="Antique map globe behind the company name"></div>
    <div class="logo-glow"></div>
    <p class="wordmark">TALLOW CREST</p>
    <div class="contact">
      <div><a href="mailto:info@tallowcrest.example">info@tallowcrest.example</a></div>
      <div>555-014-2783</div>
    </div>
    <div class="person">
      <h1 class="person__name">Gavin Torlek</h1>
      <p class="person__title">president</p>
    </div>
    <div class="qr-space" role="img" aria-label="Space reserved for QR code"></div>
  </section>
</main>
</body>
</html>
```